Home inspection business! professional look attracting customers just by looks. Read must haves

its a new business I started on my own for home inspections I would like something very professional to give to real estate agents and clients, its going to have my license number on it my business phone number my name my website as well etc on the back side it will be servicing areas and also what kind of services I offer I also have a business card from someone else the way I would like mine to be. I will attach my logo

Home Inspection

listed in nice to haves

• phone number - 555 293 8471
• website- hollowpinecheck.com
• license number #2938475610
• my name Gavin keropulis
• picture of my logo and me on the front
• on the back of the card. stating I am servicing All of New York and Long Island
• also services I will offer will be home inspection -mold inspection -lead inspection -radon inspection -Termite Inspection -Infared Scan.
• and also we provide inspections for single family homes condos co-ops town-homes
• and commercial property
• same colors as the logos and also if you recommend fonts to look like the logo not sure up to you

```html
<!DOCTYPE html>
<html lang="en">
<head>
<meta charset="utf-8">
<title>Hollow Pine Check – Business Cards</title>
<link rel="stylesheet" href="https://fonts.googleapis.com/css2?family=Roboto:wght@400;500;700&family=Titillium+Web:wght@600&display=swap">
<style>
  :root {
    --stage: #b9b9b9;
    --blue: #1a9ad9;
    --blue-deep: #0a86c9;
    --blue-ink: #1e8fd6;
    --white: #ffffff;
    --card-light: #f1f1f1;
    --grey-ink: #5f6366;
    --grey-text: #4a4d50;
    --pill: #e9e9e9;
  }
  * { box-sizing: border-box; margin: 0; padding: 0; }
  html, body { width: 1200px; height: 576px; overflow: hidden; }
  body {
    background: var(--stage);
    font-family: "Roboto", Arial, sans-serif;
    position: relative;
  }
  .card {
    position: absolute;
    border-radius: 10px;
    overflow: hidden;
  }

  /* Back: services */
  .card-back {
    left: 82px; top: 139px; width: 484px; height: 293px;
    background: linear-gradient(135deg, var(--blue) 0%, var(--blue-deep) 100%);
    color: var(--white);
    text-align: center;
  }
  .card-back .brand {
    position: absolute; left: 0; right: 0; top: 92px;
    display: flex; align-items: center; justify-content: center; gap: 10px;
    font-weight: 700; font-size: 27px; letter-spacing: 1px;
    text-transform: uppercase;
  }
  .brand-dot {
    width: 22px; height: 22px; border-radius: 50%;
    background: currentColor;
  }
  .service-area {
    position: absolute; left: 0; right: 0; top: 140px;
    font-weight: 500; font-size: 12px; letter-spacing: 2px;
    text-transform: uppercase;
  }
  .services-heading {
    position: absolute; left: 34px; right: 34px; top: 197px;
    display: flex; align-items: center; gap: 10px;
  }
  .services-heading .rule { flex: 1; height: 1px; background: rgba(255,255,255,0.75); }
  .services-heading .pill {
    background: var(--pill); color: var(--grey-ink);
    font-weight: 700; font-size: 12.5px; letter-spacing: 0.3px;
    padding: 3px 12px; border-radius: 11px;
  }
  .services-list {
    position: absolute; left: 0; right: 0; top: 227px;
    font-size: 12.6px; line-height: 16px;
  }
  .services-list .sep { margin: 0 5px; }

  /* Front: contact */
  .card-front {
    left: 602px; top: 138px; width: 480px; height: 291px;
    background: var(--card-light);
    color: var(--grey-text);
  }
  .card-front .brand {
    position: absolute; left: 24px; top: 104px;
    display: flex; align-items: center; gap: 9px;
    font-weight: 700; font-size: 22px; letter-spacing: 0.8px;
    text-transform: uppercase; color: var(--grey-ink);
  }
  .card-front .brand .brand-dot { width: 18px; height: 18px; }
  .holder-name {
    position: absolute; left: 22px; top: 162px;
    font-family: "Titillium Web", "Roboto", sans-serif;
    font-weight: 600; font-size: 20px; color: var(--blue-ink);
  }
  .holder-title {
    position: absolute; left: 22px; top: 189px;
    font-size: 12.5px; color: var(--grey-text);
  }
  .title-rule {
    position: absolute; left: 134px; top: 197px; width: 324px; height: 1.5px;
    background: var(--blue-ink);
  }
  .title-rule::after {
    content: ""; position: absolute; right: 0; bottom: 0;
    width: 1.5px; height: 12px; background: var(--blue-ink);
  }
  .corner-mark {
    position: absolute; left: 442px; top: 172px;
    width: 16px; height: 16px; border-radius: 50%;
    background: var(--grey-ink);
  }
  .contact-list {
    position: absolute; left: 24px; top: 216px;
    list-style: none; font-size: 13px; line-height: 18.5px;
  }
  .contact-list li { display: flex; align-items: center; gap: 10px; }
  .contact-list svg { width: 11px; height: 11px; fill: var(--blue-ink); }
  .contact-list .accent { color: var(--blue-ink); }
  .license {
    position: absolute; right: 22px; top: 236px;
    text-align: right; font-size: 13px; line-height: 18px;
  }
</style>
</head>
<body>

<section class="card card-back">
  <div class="brand"><span class="brand-dot"></span>Hollow Pine Check</div>
  <p class="service-area">Servicing All of New York &amp; Long Island</p>
  <div class="services-heading">
    <span class="rule"></span><span class="pill">OUR SERVICES</span><span class="rule"></span>
  </div>
  <p class="services-list">
    Home Inspection<span class="sep">|</span>Mold Inspection<span class="sep">|</span>Lead Inspection<span class="sep">|</span>Radon Inspection<br>
    Termite Inspection<span class="sep">|</span>Infared Scan<span class="sep">|</span>Single Family Homes<br>
    Condos<span class="sep">|</span>Co-ops<span class="sep">|</span>Town-homes<span class="sep">|</span>Commercial Property
  </p>
</section>

<section class="card card-front">
  <div class="brand"><span class="brand-dot"></span>Hollow Pine Check</div>
  <h1 class="holder-name">Gavin Keropulis</h1>
  <p class="holder-title">Managing Director</p>
  <span class="title-rule"></span>
  <span class="corner-mark"></span>
  <ul class="contact-list">
    <li>
      <svg viewBox="0 0 24 24" aria-hidden="true"><path d="M3 8c0-3 3-5 9-5s9 2 9 5v2h-5V7H8v3H3zM5 12h14l2 9H3z"/></svg>
      555 293 8471
    </li>
    <li>
      <svg viewBox="0 0 24 24" aria-hidden="true"><path d="M2 5h20v14H2zM3 6l9 7 9-7v2l-9 7-9-7z" fill-rule="evenodd"/></svg>
      gavin@hollowpinecheck.com
    </li>
    <li>
      <svg viewBox="0 0 24 24" aria-hidden="true"><circle cx="12" cy="12" r="10"/></svg>
      <span>www.<span class="accent">hollowpinecheck</span>.com</span>
    </li>
  </ul>
  <p class="license">License Number<br>#2938475610</p>
</section>

</body>
</html>
```